PowerPoint Design Project

We've recently updated our logo and we are in the processing of updating our web sites, business cards, letterhead, etc.

We're looking for a complete redesign of our Powerpoint template, which we have attached for reference.

Unfortunately our new web site is not released and is currently undergoing redesign so we can't send you a link to inspire.

Also attached here is our new logo.

Target Market(s)

Executives, Ph.D. scientists, researchers, venture capitalists, Board members

Industry/Entity Type

Business

```html
<!DOCTYPE html>
<html lang="en">
<head>
<meta charset="utf-8">
<title>Project Title here</title>
<link rel="stylesheet" href="https://fonts.googleapis.com/css2?family=Metrophobic&family=Open+Sans:wght@700&display=swap">
<style>
  :root {
    --brand-blue: #1b8fcb;
    --title-dark: #3c3c3c;
    --body-text: #565656;
    --canvas-bg: #f8f8f8;
    --header-top: #ffffff;
    --header-bottom: #f0f0f0;
    --rule: #dcdcdc;
  }
  * { margin: 0; padding: 0; box-sizing: border-box; }
  html, body {
    width: 1200px;
    height: 900px;
    overflow: hidden;
    background: var(--canvas-bg);
  }
  .slide {
    position: relative;
    width: 1200px;
    height: 900px;
    background: linear-gradient(180deg, #fbfbfb 0%, var(--canvas-bg) 100%);
    font-family: "Metrophobic", sans-serif;
  }
  .slide-header {
    position: absolute;
    left: 0; top: 0;
    width: 100%;
    height: 98px;
    background: linear-gradient(180deg, var(--header-top) 0%, var(--header-bottom) 100%);
    border-bottom: 2px solid var(--rule);
  }
  .slide-title {
    position: absolute;
    left: 55px;
    top: 38px;
    font-size: 40px;
    font-weight: 400;
    line-height: 1;
    color: var(--title-dark);
  }
  .slide-title .accent { color: var(--brand-blue); }
  .brand {
    position: absolute;
    right: 18px;
    top: 32px;
    display: flex;
    align-items: center;
    gap: 10px;
  }
  .brand-dot {
    width: 44px;
    height: 44px;
    border-radius: 50%;
    background: var(--brand-blue);
  }
  .brand-name {
    font-size: 38px;
    line-height: 1;
    color: var(--brand-blue);
  }
  .point-list {
    position: absolute;
    left: 55px;
    top: 170px;
    list-style: none;
  }
  .point-list li {
    display: flex;
    align-items: center;
    height: 73.5px;
    font-size: 24px;
    color: var(--body-text);
  }
  .point-list .bullet {
    flex: none;
    width: 22px;
    height: 22px;
    border-radius: 50%;
    background: var(--brand-blue);
    margin-right: 33px;
  }
  .slide-footer {
    position: absolute;
    left: 0; bottom: 0;
    width: 100%;
    height: 72px;
    border-top: 2px solid var(--rule);
    background: linear-gradient(180deg, #f3f3f3 0%, #fafafa 100%);
    font-family: "Open Sans", sans-serif;
    font-weight: 700;
    font-size: 18px;
    color: var(--brand-blue);
  }
  .page-number { position: absolute; left: 48px; top: 24px; }
  .site-address { position: absolute; right: 18px; top: 22px; }
</style>
</head>
<body>
  <main class="slide">
    <header class="slide-header">
      <h1 class="slide-title">Project <span class="accent">Title here</span></h1>
      <div class="brand">
        <span class="brand-dot"></span>
        <span class="brand-name">HelixScope</span>
      </div>
    </header>

    <ul class="point-list">
      <li><span class="bullet"></span>Lorem ipsum dolor sit ipsum Lorem ipsum dolor sit ipsum Lorem ipsum</li>
      <li><span class="bullet"></span>Lorem ipsum dolor sit ipsum Lorem ipsum dolor sit ipsum Lorem ipsum</li>
      <li><span class="bullet"></span>Lorem ipsum dolor sit ipsum Lorem ipsum dolor sit ipsum Lorem ipsum</li>
      <li><span class="bullet"></span>Lorem ipsum dolor sit ipsum Lorem ipsum dolor sit ipsum Lorem ipsum</li>
      <li><span class="bullet"></span>Lorem ipsum dolor sit ipsum Lorem ipsum dolor sit ipsum Lorem ipsum</li>
      <li><span class="bullet"></span>Lorem ipsum dolor sit ipsum Lorem ipsum dolor sit ipsum Lorem ipsum</li>
    </ul>

    <footer class="slide-footer">
      <span class="page-number">Page No. 00</span>
      <span class="site-address">www.helixscope.com</span>
    </footer>
  </main>
</body>
</html>
```